An effective double sided Marketing Postcard Design with a compelling call to action

I want to design an oversized postcard that can be mailed without an envelope. I want a postcard that that inspires and also informs people of when to cal me "If this is happening...call me" I am attaching this file but know I am open to any other ideas. Enclosed is one image, logo and picture and services if they fit anywhere. I like the picture of the one girl with gloves or will be open to using both the boy and the girl.I enclosed the text to go on the front and the back of the card in a word doc, not sure how many will fit on the back of the card. I'd like it to appear like these do: http://www.dailyvelmorpress.com/2014/12/19/super-hero-inspirational-quotes_n_6272328.html

Target Market(s)

Executives, Technology leaders, CIO's, CMO's, Managers

Industry/Entity Type

Information Technology

Font styles to use
Serif

Colors
33a6d7
f04a50

Requirements
Must have
• A fun graphic image or cartoon that makes the person laugh or smile. A great layout of the "When " " is happening Call me!" I'd like to have it be something they will keep in their desk for reference or they will immediately call.
• Use my brand colors which are attached. Use the font similar to the brand color guide for headlines.
Nice to have
• An oversized card designed.
Should not have
• typos or misaligned sentences

```html
<!DOCTYPE html>
<html lang="en">
<head>
<meta charset="utf-8">
<title>Brightwater Leadership Group – Postcard</title>
<link rel="stylesheet" href="https://fonts.googleapis.com/css2?family=Tinos:ital,wght@0,400;0,700;1,400&display=swap">
<style>
  :root {
    --brand-blue: #33a6d7;
    --brand-red: #f04a50;
    --sky-light: #eaf5fb;
    --sky-mid: #a9d6ee;
    --sky-deep: #3f8fc4;
    --list-bg: #dcf0f9;
    --call-bg: #fbd6d8;
    --ink: #2b2b2b;
    --page: #e9ecef;
    --card: #ffffff;
  }
  * { box-sizing: border-box; margin: 0; padding: 0; }
  html, body { width: 800px; height: 1200px; overflow: hidden; }
  body {
    background: var(--page);
    font-family: "Tinos", "Times New Roman", serif;
    color: var(--ink);
    position: relative;
  }
  .postcard {
    position: absolute;
    left: 50px;
    width: 700px;
    height: 450px;
    background: var(--card);
    box-shadow: 0 4px 14px rgba(0,0,0,.18);
    overflow: hidden;
  }
  .postcard--front { top: 130px; }
  .postcard--back { top: 650px; }

  /* Front */
  .hero-photo {
    position: absolute; inset: 0;
    background:
      radial-gradient(ellipse at 30% 55%, rgba(240,74,80,.35) 0, rgba(240,74,80,0) 38%),
      linear-gradient(160deg, var(--sky-deep) 0%, var(--sky-mid) 45%, var(--sky-light) 100%);
  }
  .brand {
    position: absolute; top: 34px; right: 30px; width: 390px; text-align: center;
  }
  .brand__name {
    display: inline-flex; align-items: center; gap: 10px;
    font-size: 26px; font-weight: 400; color: var(--brand-red);
  }
  .brand__dot {
    width: 14px; height: 14px; border-radius: 50%; background: var(--brand-red);
  }
  .brand__tagline {
    font-size: 14px; font-style: italic; color: var(--brand-blue); margin-top: 8px;
  }
  .headline {
    position: absolute; right: 20px; bottom: 40px; width: 410px;
    font-weight: 700; line-height: 1.25; text-align: center;
  }
  .headline__call { display: block; color: var(--brand-red); font-size: 20px; margin-bottom: 4px; }
  .headline__body { display: block; color: var(--brand-blue); font-size: 22px; }

  /* Back */
  .when-panel {
    position: absolute; left: 26px; top: 28px; width: 600px; height: 250px;
    background: var(--list-bg); border-radius: 14px; padding: 10px 18px;
  }
  .when-panel__label { color: var(--brand-red); font-weight: 700; font-size: 12px; }
  .when-list { list-style: none; font-size: 11.5px; line-height: 16.5px; }
  .when-list li { color: var(--brand-blue); }
  .when-list li::before { content: "\2192\00a0"; color: var(--brand-red); }
  .when-list li:nth-child(odd) { color: var(--brand-red); }
  .call-panel {
    position: absolute; left: 26px; top: 290px; width: 600px; height: 130px;
    background: var(--call-bg); border-radius: 14px; padding: 12px 18px;
    font-size: 11.5px; line-height: 16px; color: var(--ink);
  }
  .call-panel__head { color: var(--brand-red); font-weight: 700; }
  .call-panel__head em { font-weight: 400; }
  .call-panel__sign { margin-top: 8px; }
</style>
</head>
<body>
  <section class="postcard postcard--front">
    <div class="hero-photo" role="img" aria-label="Photo of a young child in a red cape, blue mask and red boxing gloves punching forward against a blue sky"></div>
    <div class="brand">
      <div class="brand__name"><span class="brand__dot"></span>Brightwater Leadership Group</div>
      <div class="brand__tagline">Relevant Trailblazer Strategies to Produce Real Results</div>
    </div>
    <h1 class="headline">
      <span class="headline__call">Activate your Inner Trailblazer Leader!</span>
      <span class="headline__body">When you want super hero results,<br>you find friends<br>in unexpected places.</span>
    </h1>
  </section>

  <section class="postcard postcard--back">
    <div class="when-panel">
      <div class="when-panel__label">WHEN:</div>
      <ul class="when-list">
        <li>it is taking twice as long to get things done due to turf wars</li>
        <li>you are tired of key initiatives not being followed</li>
        <li>you are asked to play an unwinnable game</li>
        <li>you are frustrated with a dominant person causing delays</li>
        <li>you need your team to play full out in a high stakes game</li>
        <li>you find your people "sleepwalking" instead of taking a lead</li>
        <li>you don't want to pay for the same mistake twice by doing costly rework</li>
        <li>you don't have the time to be creative</li>
        <li>you are exhausted by a calendar overbooked with meetings</li>
        <li>you need to be more visible within the organization</li>
        <li>you want to navigate internal and external politics with ease</li>
        <li>you want to be seen as a valued member of the organization</li>
        <li>you want to lead with influence, impact and ingenuity using your unique super powers!</li>
      </ul>
    </div>
    <div class="call-panel">
      <p class="call-panel__head">CALL ME! 555-014-7371 <em>Dana@brightwaterlead.com</em></p>
      <p>Run with the Trailblazers. Stand out from the Crowd. Join our many clients who gain fuel for personal, professional and business results. Ask me how you can activate your super powers!</p>
      <p class="call-panel__sign">Dana Merriweather<br>Brightwater Leadership Group, Ashford NH</p>
    </div>
  </section>
</body>
</html>
```